Bring to life the sophistication and high-level expertise of my consulting business

I am looking for a sleek, modern, sharp PowerPoint design package, with options for a wide range of slide types.
We would like our logo/graphic and its colors (a blue pallet) to be prominently featured. The design should communicate expertise, sophistication, executive-level of work, be bold and look clean and sleek at the same time. There should be no doubt this was professionally done.
The font that will best work with this logo is a basic font using AvantGarde BkBt (custom)
Company briefing:
A consulting and advisory practice specialized in the Consumer Goods and Services Industries. Our methodology is distinguished by its ability to transform visionary thinking—be it blue-sky ideas, inspiration, or innovation—into practical strategies. We drive initiatives aimed at driving revenue growth and enhancing profit margins using 3 pillars: THE PEOPLE, THE CUSTOMER EXPERIENCE and THE OPERATING PLATFORM.
Target audiences are in 3 key areas: C-suite executives (owners and decision-makers of small to mid-cap companies), partners in larger Consulting Companies and Investment Firms (Private Equity/Venture capital, etc)

*In addition to the PowerPoint package, I would like a quote for designs for an email signature, a Microsoft Word template, and a company LinkedIn page (all in the same style as the PPT template)
Updates

Low design quality

Target Market(s)

Target audiences are in 3 key areas: C-suite executives (owners and decision-makers), partners in larger Consulting Companies and Investment Firms (Private Equity/Venture capital, etc.)

Industry/Entity Type

Business Consulting and Advisory

Font styles to use
Sans Serif
Other font styles liked:
• The font that will work best with the logo is basic font using AvantGarde BkBt (custom)

Colors
0054AA
0677BA
7BADD7
CADEEF
E8F1F8
0094D4
00A9DD
6FCCEA
C7EBF8
E9F6FB

Requirements
Must have
• We would like our logo, the graphic shapes and its colors (a blue pallet) to be prominently featured. The design should communicate expertise, sophistication, executive-level of work. It should be sleek, modern, bold and unique.
Nice to have
• A large number of slide options for each type of slide as part of the package
Should not have
• it should not look busy, generic or too traditional

```html
<!DOCTYPE html>
<html lang="en">
<head>
<meta charset="utf-8">
<title>Cadencia – Presentation Template</title>
<link href="https://fonts.googleapis.com/css2?family=Montserrat:wght@500;600;700;800&family=Roboto:wght@400;500;700&display=swap" rel="stylesheet">
<style>
  :root{
    --navy:#0054AA;
    --blue:#0677BA;
    --sky:#0094D4;
    --cyan:#00A9DD;
    --cyan-soft:#6FCCEA;
    --ice:#E9F6FB;
    --ink:#222831;
    --body:#3a3f47;
    --canvas:#dcdcdc;
    --white:#ffffff;
  }
  *{box-sizing:border-box;margin:0;padding:0}
  html,body{width:1200px;height:3966px;overflow:hidden}
  body{background:var(--canvas);position:relative;font-family:"Roboto",Arial,sans-serif;color:var(--body)}
  .slide{position:absolute;left:86px;width:1028px;height:579px;overflow:hidden;background:var(--white);box-shadow:0 2px 8px rgba(0,0,0,.12)}
  .slide--blue{background:linear-gradient(160deg,#0aa3e3 0%,#0a86d2 45%,var(--navy) 100%);color:var(--white)}

  /* brand name lockup */
  .brand{position:absolute;display:flex;align-items:center;gap:12px;font-family:"Montserrat",Arial,sans-serif;font-weight:600;letter-spacing:.32em;color:var(--blue)}
  .brand__dot{width:16px;height:16px;border-radius:50%;background:var(--sky)}
  .brand--light{color:var(--white)}
  .brand--light .brand__dot{background:var(--white)}
  .brand--small{font-size:18px;left:794px;top:38px}

  /* headings */
  .slide-title{position:absolute;left:63px;top:18px;font-family:"Montserrat",Arial,sans-serif;font-weight:700;font-size:31px;color:var(--ink);letter-spacing:-.01em}
  .slide--blue .slide-title{color:var(--white)}
  .title-rule{position:absolute;left:0;top:70px;width:164px;height:2px;background:var(--cyan)}
  .title-rule::after{content:"";position:absolute;right:-3px;top:-3px;width:8px;height:8px;border-radius:50%;background:var(--cyan)}
  .slide--blue .title-rule,.slide--blue .title-rule::after{background:var(--white)}

  /* footer */
  .footer{position:absolute;left:0;bottom:18px;width:734px;height:48px;background:var(--cyan);color:var(--white);font-size:15px;display:flex;align-items:center;padding-left:59px}
  .page-no{position:absolute;left:712px;bottom:18px;width:48px;height:48px;border-radius:50%;background:var(--white);border:3px solid var(--cyan);color:var(--ink);font-size:18px;display:flex;align-items:center;justify-content:center}

  .photo{position:absolute;background:linear-gradient(135deg,#d9d3cb,#a8b3bd 55%,#6f7b88)}

  /* slide 1 */
  .cover{top:86px}
  .cover .brand{left:62px;top:62px;font-size:22px}
  .cover__eyebrow{position:absolute;left:62px;top:244px;font-family:"Montserrat",Arial,sans-serif;font-weight:600;font-size:27px;color:var(--white)}
  .cover__title{position:absolute;left:60px;top:288px;font-family:"Montserrat",Arial,sans-serif;font-weight:800;font-size:66px;color:var(--white);letter-spacing:-.01em}
  .cover__lead{position:absolute;left:62px;top:376px;width:420px;font-size:12.5px;line-height:22px;color:var(--white)}
  .cover__photo{position:absolute;left:506px;top:-160px;width:710px;height:710px;border-radius:50%;border:9px solid var(--white);background:linear-gradient(140deg,#efe9e1,#c9b7a2 45%,#6d7884)}

  /* slide 2 */
  .about{top:730px}
  .about .photo{left:62px;top:112px;width:434px;height:366px}
  .about__text{position:absolute;left:532px;top:140px;width:441px;font-size:17.5px;line-height:34.5px;text-align:justify}

  /* slide 3 */
  .pillars{top:1373px}
  .pillar{position:absolute;top:185px;width:288px;height:271px;background:var(--white);border-radius:10px;box-shadow:0 4px 16px rgba(0,0,0,.1);text-align:center;padding:64px 14px 0}
  .pillar__icon{position:absolute;left:50%;top:-46px;margin-left:-46px;width:92px;height:92px;border-radius:50%;background:var(--blue);display:flex;align-items:center;justify-content:center}
  .pillar__title{font-family:"Roboto",Arial,sans-serif;font-weight:500;font-size:19.5px;color:var(--ink);margin-bottom:4px}
  .pillar__text{font-size:15px;line-height:30px;color:var(--body)}

  /* slide 4 */
  .services{top:2016px}
  .services .brand--small{color:var(--white)}
  .services .brand__dot{background:var(--white)}
  .service{position:absolute;width:277px;height:180px;border:1.5px solid rgba(255,255,255,.55);border-radius:10px;background:rgba(255,255,255,.06);padding:18px 16px}
  .service__head{display:flex;align-items:center;gap:12px;margin-bottom:16px}
  .service__icon{width:56px;height:56px;border-radius:50%;border:1.5px solid rgba(255,255,255,.8);display:flex;align-items:center;justify-content:center;flex:none}
  .service__title{font-weight:700;font-size:13px}
  .service__text{font-size:12.5px;line-height:23px}

  /* slide 5 */
  .why{top:2660px}
  .why__text{position:absolute;left:56px;top:148px;width:466px;font-size:17.5px;line-height:34.5px;text-align:justify}
  .why__photo{position:absolute;left:560px;top:92px;width:414px;height:414px;border-radius:50%;border:5px solid var(--sky);background:linear-gradient(135deg,#cfd6dc,#a89783 50%,#5f6f80)}

  /* slide 6 */
  .closing{top:3304px}
  .closing .brand{left:0;right:0;justify-content:center;top:160px;font-size:44px;gap:22px}
  .closing .brand__dot{width:30px;height:30px}
  .closing__title{position:absolute;left:0;right:0;top:310px;text-align:center;font-family:"Montserrat",Arial,sans-serif;font-weight:800;font-size:80px;color:var(--white)}
</style>
</head>
<body>

<!-- Cover -->
<section class="slide slide--blue cover">
  <div class="brand brand--light"><span class="brand__dot"></span>CADENCIA</div>
  <p class="cover__eyebrow">WELCOME TO</p>
  <h1 class="cover__title">CADENCIA</h1>
  <p class="cover__lead">Lorem ipsum dolor sit amet, consectetur adipiscing elit sed eiusmod tempor incididunt ut labore et dolore magna aliqua enim ad minim.</p>
  <div class="cover__photo" role="img" aria-label="Photo of a smiling consultant in a meeting with a client at a laptop"></div>
</section>

<!-- About -->
<section class="slide about">
  <h2 class="slide-title">ABOUT US</h2>
  <div class="title-rule"></div>
  <div class="brand brand--small"><span class="brand__dot"></span>CADENCIA</div>
  <div class="photo" role="img" aria-label="Photo of an advisor reviewing documents with a client"></div>
  <p class="about__text">Lorem ipsum dolor sit amet, consectetur adipiscing elit, sed do eiusmod tempor incididunt ut labore et dolore magna aliqua. Ut enim ad minim veniam, quis nostrud exercitation ullamco laboris nisi ut aliquip ex ea commodo consequat. Duis aute irure dolor in reprehenderit in voluptate velit esse cillum dolore eu fugiat nulla pariatur. Excepteur sint occaecat cupidatat non proident, sunt in culpa qui officia deserunt mollit anim id est laborum</p>
  <div class="footer">© 2024 Cadencia. All Rights Reserved</div>
  <div class="page-no">02</div>
</section>

<!-- Pillars -->
<section class="slide pillars">
  <h2 class="slide-title">OUR 3 PILLARS</h2>
  <div class="title-rule"></div>
  <div class="brand brand--small"><span class="brand__dot"></span>CADENCIA</div>

  <div class="pillar" style="left:63px">
    <div class="pillar__icon"><svg width="46" height="46" viewBox="0 0 46 46" fill="#fff"><circle cx="23" cy="15" r="9"/><path d="M7 42c0-10 7-16 16-16s16 6 16 16z"/></svg></div>
    <h3 class="pillar__title">THE PEOPLE</h3>
    <p class="pillar__text">Lorem ipsum dolor sit ameted consectetur adipiscing elit sed do eiusmod tempor incididunt ut labore et dolore magna aliquat enim ad minim veniam.</p>
  </div>
  <div class="pillar" style="left:374px">
    <div class="pillar__icon"><svg width="52" height="46" viewBox="0 0 52 46" fill="#fff"><circle cx="26" cy="20" r="6"/><circle cx="14" cy="22" r="4.5"/><circle cx="38" cy="22" r="4.5"/><path d="M16 42c0-7 4-12 10-12s10 5 10 12z"/><path d="M5 40c0-6 4-10 9-10 2 0 3 .5 4 1-2 2-3 5-3 9z"/><path d="M47 40c0-6-4-10-9-10-2 0-3 .5-4 1 2 2 3 5 3 9z"/><path d="M15 4l1.5 3 3 .4-2.2 2 .6 3-2.9-1.5-2.9 1.5.6-3-2.2-2 3-.4zM26 2l1.5 3 3 .4-2.2 2 .6 3L26 9l-2.9 1.5.6-3-2.2-2 3-.4zM37 4l1.5 3 3 .4-2.2 2 .6 3-2.9-1.5-2.9 1.5.6-3-2.2-2 3-.4z"/></svg></div>
    <h3 class="pillar__title">THE CUSTOMER EXPERIENCE</h3>
    <p class="pillar__text">Lorem ipsum dolor sit ameted consectetur adipiscing elit sed do eiusmod tempor incididunt ut labore et dolore magna aliquat enim ad minim veniam.</p>
  </div>
  <div class="pillar" style="left:684px">
    <div class="pillar__icon"><svg width="50" height="46" viewBox="0 0 50 46" fill="none" stroke="#fff" stroke-width="2.5"><rect x="4" y="5" width="42" height="28" rx="2"/><path d="M18 42h14M25 33v9"/><circle cx="25" cy="17" r="5"/><path d="M16 29c1-5 5-7 9-7s8 2 9 7"/></svg></div>
    <h3 class="pillar__title">THE OPERATING PLATFORM.</h3>
    <p class="pillar__text">Lorem ipsum dolor sit ameted consectetur adipiscing elit sed do eiusmod tempor incididunt ut labore et dolore magna aliquat enim ad minim veniam.</p>
  </div>

  <div class="footer">© 2024 Cadencia. All Rights Reserved</div>
  <div class="page-no">03</div>
</section>

<!-- Services -->
<section class="slide slide--blue services" role="img" aria-label="Services slide over a blue-tinted photo of a business team">
  <h2 class="slide-title">OUR SERVICES</h2>
  <div class="title-rule"></div>
  <div class="brand brand--small"><span class="brand__dot"></span>CADENCIA</div>

  <div class="service" style="left:63px;top:108px">
    <div class="service__head"><span class="service__icon"><svg width="28" height="28" viewBox="0 0 28 28" fill="none" stroke="#fff" stroke-width="1.6"><circle cx="14" cy="9" r="5"/><path d="M5 26c0-6 4-10 9-10s9 4 9 10"/></svg></span><span class="service__title">Lorem ipsum dolor sit amet</span></div>
    <p class="service__text">Lorem ipsum dolor sit amet consectetur adipiscing elited sed do eiusmod tempor incididunt ut labore eted dolore magnd.</p>
  </div>
  <div class="service" style="left:379px;top:108px">
    <div class="service__head"><span class="service__icon"><svg width="28" height="28" viewBox="0 0 28 28" fill="none" stroke="#fff" stroke-width="1.6"><rect x="3" y="4" width="22" height="15" rx="1"/><path d="M7 15l5-5 4 3 5-5M10 24h8"/></svg></span><span class="service__title">Lorem ipsum dolor sit amet</span></div>
    <p class="service__text">Lorem ipsum dolor sit amet consectetur adipiscing elited sed do eiusmod tempor incididunt ut labore eted dolore magnd.</p>
  </div>
  <div class="service" style="left:695px;top:108px">
    <div class="service__head"><span class="service__icon"><svg width="28" height="28" viewBox="0 0 28 28" fill="none" stroke="#fff" stroke-width="1.6"><circle cx="14" cy="12" r="8"/><path d="M14 7v5l3 3M9 25h10"/></svg></span><span class="service__title">Lorem ipsum dolor sit amet</span></div>
    <p class="service__text">Lorem ipsum dolor sit amet consectetur adipiscing elited sed do eiusmod tempor incididunt ut labore eted dolore magnd.</p>
  </div>
  <div class="service" style="left:63px;top:305px">
    <div class="service__head"><span class="service__icon"><svg width="28" height="28" viewBox="0 0 28 28" fill="none" stroke="#fff" stroke-width="1.6"><rect x="4" y="4" width="16" height="20" rx="1"/><path d="M8 10h8M8 14h8M8 18h5"/><circle cx="21" cy="20" r="4"/></svg></span><span class="service__title">Lorem ipsum dolor sit amet</span></div>
    <p class="service__text">Lorem ipsum dolor sit amet consectetur adipiscing elited sed do eiusmod tempor incididunt ut labore eted dolore magnd.</p>
  </div>
  <div class="service" style="left:379px;top:305px">
    <div class="service__head"><span class="service__icon"><svg width="28" height="28" viewBox="0 0 28 28" fill="none" stroke="#fff" stroke-width="1.6"><circle cx="10" cy="9" r="4"/><circle cx="19" cy="9" r="4"/><path d="M3 24c0-5 3-8 7-8s7 3 7 8M13 19c1-2 3-3 6-3 4 0 6 3 6 8"/></svg></span><span class="service__title">Lorem ipsum dolor sit amet</span></div>
    <p class="service__text">Lorem ipsum dolor sit amet consectetur adipiscing elited sed do eiusmod tempor incididunt ut labore eted dolore magnd.</p>
  </div>
  <div class="service" style="left:695px;top:305px">
    <div class="service__head"><span class="service__icon"><svg width="28" height="28" viewBox="0 0 28 28" fill="none" stroke="#fff" stroke-width="1.6"><rect x="4" y="5" width="20" height="14" rx="1"/><circle cx="14" cy="12" r="3"/><path d="M9 24l5-5 5 5"/></svg></span><span class="service__title">Lorem ipsum dolor sit amet</span></div>
    <p class="service__text">Lorem ipsum dolor sit amet consectetur adipiscing elited sed do eiusmod tempor incididunt ut labore eted dolore magnd.</p>
  </div>

  <div class="footer">© 2024 Cadencia. All Rights Reserved</div>
  <div class="page-no">04</div>
</section>

<!-- Why choose us -->
<section class="slide why">
  <h2 class="slide-title">WHY CHOOSE US?</h2>
  <div class="title-rule"></div>
  <div class="brand brand--small"><span class="brand__dot"></span>CADENCIA</div>
  <p class="why__text">Lorem ipsum dolor sit amet, consectetur adipiscing elit, sed do eiusmod tempor incididunt ut labore et dolore magna aliqua. Ut enim ad minim veniam, quis nostrud exercitation ullamco laboris nisi ut aliquip ex ea commodo consequat. Duis aute irure dolor in reprehenderit in voluptate velit esse cillum dolore eu fugiat nulla pariatur. Excepteur sint occaecat cupidatat non proident, sunt in culpa qui officia deserunt mollit anim id est laborum exercitation ullamco laboris.</p>
  <div class="why__photo" role="img" aria-label="Photo of a smiling business team around a meeting table"></div>
  <div class="footer">© 2024 Cadencia. All Rights Reserved</div>
  <div class="page-no">05</div>
</section>

<!-- Closing -->
<section class="slide slide--blue closing">
  <div class="brand brand--light"><span class="brand__dot"></span>CADENCIA</div>
  <p class="closing__title">THANK YOU</p>
  <div class="footer">© 2024 Cadencia. All Rights Reserved</div>
  <div class="page-no">06</div>
</section>

</body>
</html>
```